Business card design for Birch Engineering Torvant

We need a new business card design along with all the necessary to place an order. The company is Birch Engineering Torvant and we recently updated our logo.

```html
<!DOCTYPE html>
<html lang="en">
<head>
<meta charset="UTF-8">
<title>Birch Engineering Torvant – Business Card</title>
<link href="https://fonts.googleapis.com/css2?family=Poppins:wght@400;600&display=swap" rel="stylesheet">
<style>
  :root {
    --bg: #1d1d1d;
    --card-white: #ffffff;
    --card-grey: #959595;
    --brand-yellow: #dfbd22;
    --brand-grey: #8f8f8f;
    --text-grey: #8a8a8a;
    --divider: #b5b5b5;
  }
  * { margin: 0; padding: 0; box-sizing: border-box; }
  html, body {
    width: 1093px; height: 1200px; overflow: hidden;
    background: var(--bg);
    font-family: "Poppins", sans-serif;
  }
  .canvas { position: relative; width: 1093px; height: 1200px; }

  .card {
    position: absolute; left: 265px; width: 578px; height: 356px;
    border-radius: 26px; overflow: hidden;
  }
  .card--front { top: 226px; background: var(--card-white); }
  .card--back { top: 621px; background: var(--card-grey); }

  .wordmark {
    position: absolute; display: flex; align-items: center;
    font-weight: 600; white-space: nowrap;
  }
  .wordmark__square { background: var(--brand-yellow); flex: none; }
  .card--front .wordmark { left: 28px; top: 166px; gap: 10px; color: var(--brand-grey); font-size: 15.5px; }
  .card--front .wordmark__square { width: 14px; height: 14px; }
  .card--back .wordmark { left: 0; right: 0; top: 158px; justify-content: center; gap: 14px; color: #ffffff; font-size: 29px; }
  .card--back .wordmark__square { width: 24px; height: 24px; }

  .divider {
    position: absolute; left: 288px; top: 75px; width: 1.5px; height: 208px;
    background: linear-gradient(to bottom, rgba(181,181,181,0), var(--divider) 20%, var(--divider) 80%, rgba(181,181,181,0));
  }

  .contact { position: absolute; left: 311px; top: 89px; color: var(--text-grey); }
  .contact__name { font-weight: 600; font-size: 22.5px; line-height: 1.1; letter-spacing: -0.2px; }
  .contact__title { color: var(--brand-yellow); font-size: 17px; line-height: 1.15; }
  .contact__list { list-style: none; margin-top: 12px; }
  .contact__item { display: flex; align-items: center; gap: 7px; font-size: 17px; line-height: 21px; }
  .contact__icon { width: 15px; height: 15px; flex: none; fill: var(--brand-yellow); }
  .contact__address { margin-top: 13px; font-size: 17px; line-height: 21px; }

  .card__band { position: absolute; left: 0; bottom: 0; width: 100%; height: 13px; }
</style>
</head>
<body>
<div class="canvas">

  <section class="card card--front" aria-label="Business card front">
    <div class="wordmark">
      <span class="wordmark__square"></span>
      <span class="wordmark__name">Birch Engineering Torvant</span>
    </div>

    <div class="divider"></div>

    <div class="contact">
      <h1 class="contact__name">DANIEL MARSH</h1>
      <p class="contact__title">Managing Director</p>
      <ul class="contact__list">
        <li class="contact__item">
          <svg class="contact__icon" viewBox="0 0 24 24" aria-hidden="true"><path d="M6.6 10.8a15.1 15.1 0 0 0 6.6 6.6l2.2-2.2c.3-.3.7-.4 1-.2 1.1.4 2.3.6 3.6.6.6 0 1 .4 1 1V20c0 .6-.4 1-1 1A17 17 0 0 1 3 4c0-.6.4-1 1-1h3.5c.6 0 1 .4 1 1 0 1.3.2 2.5.6 3.6.1.3 0 .7-.2 1z"/></svg>
          <span>044-310 872 554</span>
        </li>
        <li class="contact__item">
          <svg class="contact__icon" viewBox="0 0 24 24" aria-hidden="true"><path d="M2 5h20v14H2z M3.5 6.5 12 13l8.5-6.5" fill="var(--brand-yellow)" stroke="#fff" stroke-width="1.4"/></svg>
          <span>hello@birchtorvant.com</span>
        </li>
        <li class="contact__item">
          <svg class="contact__icon" viewBox="0 0 24 24" aria-hidden="true"><circle cx="12" cy="12" r="10"/><path d="M2 12h20M12 2c3 3 3 17 0 20M12 2c-3 3-3 17 0 20M4 7h16M4 17h16" fill="none" stroke="#fff" stroke-width="1.3"/></svg>
          <span>www.birchtorvant.com</span>
        </li>
      </ul>
      <p class="contact__address">421, Address line goes here<br>45452,Country Name</p>
    </div>

    <svg class="card__band" viewBox="0 0 578 13" preserveAspectRatio="none" aria-hidden="true">
      <polygon points="0,0 290,0 285,13 0,13" fill="var(--brand-yellow)"/>
      <polygon points="290,0 293,0 288,13 285,13" fill="#ffffff"/>
      <polygon points="293,0 578,0 578,13 288,13" fill="var(--brand-grey)"/>
    </svg>
  </section>

  <section class="card card--back" aria-label="Business card back">
    <div class="wordmark">
      <span class="wordmark__square"></span>
      <span class="wordmark__name">Birch Engineering Torvant</span>
    </div>
  </section>

</div>
</body>
</html>
```